Food Choices & Patient-Reported Outcomes in Parkinson's disease

We have spent the past 7 years studying food choices and rate of PD progression. We want to show people which foods have the most significant impact. <br/><br/>The infographic attached called "Kindred Living in QT" is the first in this 6-part series, recently designed by someone on PixelGuild. I'd like this entire series to "pair nicely" with one another, but also have unique personality, which is why I've opened the contest up. <br/><br/>The VEX-QT scale is the point of reference, it explains that higher scores are worse, low scores are better. I'd like to stick with the green is good, red is bad theme. ish. <br/><br/>The blue bar chart with food is "the grand finale." THIS is the information people have been waiting for for decades! I expect this to be highly circulated-- passed to physicians, support groups, getting tens of thousands of shares online! Below, I uploaded the 2019 version (also produced by someone from Pixel Guild). On my ppt screen shot, that data on the bottom left is also REALLY important. Can make another bar chart? Or find some other creative way to communicate it? OK to not include the p-values (OK to remove the far right column). Thanks!

Target Market(s)

Patients, their partners/ families, and health care providers.

Requirements
Must have
• Must include the legend-- some version of the VEX-QT scale vs. Quality of Life, as a point of reference. If possible, I'd like to stick with [some shade of] green is good, with it being clear that scores are getting worse [red-ish] as the scores increase.
• Must have the website, so people can go look for more information/ details about the project.
Nice to have
• Coordination with the "Kindred Living ..." infographic below.

```html
<!DOCTYPE html>
<html lang="en">
<head>
<meta charset="utf-8">
<title>Food Choices &amp; Patient-Reported Outcomes in Parkinson's Disease</title>
<link href="https://fonts.googleapis.com/css2?family=Catamaran:wght@400;500;600;700&family=Cardo:wght@400;700&display=swap" rel="stylesheet">
<style>
  :root {
    --bg-deep: #2f2c52;
    --bg-mid: #46427a;
    --header-tint: #5a5892;
    --panel: #ffffff;
    --panel-soft: #f4f3ef;
    --band-head: #7e7b97;
    --ink: #4a4a4a;
    --ink-soft: #8c8c8c;
    --navy: #283184;
    --red: #f2705a;
    --red-soft: #f6a57e;
    --green: #7dbd5a;
    --green-bright: #27b36b;
    --green-soft: #c2e1a3;
    --green-mid: #92cd6c;
    --track: #e3e3e8;
    --sky: #a9c9f2;
    --sans: "Catamaran", sans-serif;
    --serif: "Cardo", serif;
  }
  html, body { margin: 0; padding: 0; overflow: hidden; }
  body { background: var(--bg-deep); }
  .canvas {
    position: relative; width: 1200px; height: 848px; overflow: hidden;
    background: linear-gradient(120deg, var(--bg-mid), var(--bg-deep));
    font-family: var(--sans);
  }
  .header-tab {
    position: absolute; left: 0; top: 0; width: 695px; height: 120px;
    background: var(--header-tint); border-radius: 0 90px 0 0;
  }
  .main-title {
    position: absolute; left: 66px; top: 30px; margin: 0;
    color: #fff; font-weight: 700; font-size: 29px; line-height: 35px;
  }
  .year { position: absolute; left: 555px; top: 50px; color: #8c8ab8; font-size: 34px; font-weight: 600; }
  .side-title {
    position: absolute; right: 52px; top: 48px; margin: 0; text-align: right;
    color: var(--sky); font-size: 26px; font-weight: 500; line-height: 29px;
  }
  .side-title strong { font-weight: 700; color: #dbe8fb; }
  .panel { position: absolute; }
  .panel svg { display: block; }
  .panel-correlation { left: 16px; top: 120px; width: 688px; height: 378px; background: var(--panel); }
  .panel-servings { left: 708px; top: 120px; width: 476px; height: 688px; background: var(--panel); border-radius: 0 0 24px 24px; }
  .panel-behaviors { left: 16px; top: 498px; width: 624px; height: 338px; background: var(--panel-soft); }
  .footer-tab {
    position: absolute; left: 702px; top: 810px; width: 498px; height: 38px;
    background: #2a2748; border-radius: 28px 0 0 0;
    color: #fff; font-family: var(--serif); font-weight: 700; font-size: 19px;
    letter-spacing: 1px; line-height: 38px; text-align: center;
  }
  .serif { font-family: var(--serif); }
  .sans { font-family: var(--sans); }
</style>
</head>
<body>
<div class="canvas">
  <div class="header-tab"></div>
  <h1 class="main-title">Food Choices &amp; Patient-Reported<br>Outcomes in Parkinson's Disease</h1>
  <div class="year">2020</div>
  <h2 class="side-title">Impact of <strong>2-4 Servings Per Week</strong><br>On Parkinson's Disease Severity</h2>

  <!-- Correlation panel -->
  <section class="panel panel-correlation">
    <svg width="688" height="378" viewBox="20 150 860 472">
      <text x="76" y="190" class="serif" font-size="28" fill="#555" letter-spacing="1">Correlation between Quality of life &amp; VEX-QT score</text>
      <g class="band-fills">
        <rect x="158" y="210" width="442" height="128" fill="var(--red)"/>
        <rect x="158" y="338" width="442" height="62" fill="var(--red-soft)"/>
        <rect x="158" y="400" width="442" height="68" fill="var(--green-soft)"/>
        <rect x="158" y="468" width="442" height="62" fill="var(--green-mid)"/>
      </g>
      <g class="grid" stroke="#fff" stroke-width="2">
        <line x1="212" y1="210" x2="212" y2="530"/><line x1="277" y1="210" x2="277" y2="530"/>
        <line x1="342" y1="210" x2="342" y2="530"/><line x1="407" y1="210" x2="407" y2="530"/>
        <line x1="472" y1="210" x2="472" y2="530"/><line x1="537" y1="210" x2="537" y2="530"/>
        <line x1="158" y1="272" x2="600" y2="272"/><line x1="158" y1="338" x2="600" y2="338"/>
        <line x1="158" y1="400" x2="600" y2="400"/><line x1="158" y1="468" x2="600" y2="468"/>
      </g>
      <g class="scatter" fill="#fff">
        <circle cx="162" cy="235" r="2.5"/><circle cx="180" cy="280" r="2.5"/><circle cx="196" cy="300" r="2.5"/><circle cx="230" cy="262" r="2.5"/><circle cx="258" cy="255" r="2.5"/><circle cx="282" cy="245" r="2.5"/><circle cx="300" cy="290" r="2.5"/><circle cx="318" cy="268" r="2.5"/><circle cx="335" cy="330" r="2.5"/><circle cx="378" cy="298" r="2.5"/><circle cx="426" cy="264" r="2.5"/><circle cx="452" cy="322" r="2.5"/><circle cx="212" cy="315" r="2.5"/><circle cx="240" cy="300" r="2.5"/><circle cx="290" cy="320" r="2.5"/><circle cx="188" cy="318" r="2.5"/>
        <circle cx="170" cy="345" r="2.5"/><circle cx="185" cy="352" r="2.5"/><circle cx="200" cy="360" r="2.5"/><circle cx="215" cy="348" r="2.5"/><circle cx="232" cy="362" r="2.5"/><circle cx="250" cy="356" r="2.5"/><circle cx="268" cy="370" r="2.5"/><circle cx="285" cy="350" r="2.5"/><circle cx="302" cy="366" r="2.5"/><circle cx="322" cy="380" r="2.5"/><circle cx="345" cy="360" r="2.5"/><circle cx="372" cy="352" r="2.5"/><circle cx="396" cy="378" r="2.5"/><circle cx="430" cy="365" r="2.5"/><circle cx="585" cy="355" r="2.5"/><circle cx="176" cy="372" r="2.5"/><circle cx="205" cy="386" r="2.5"/><circle cx="240" cy="382" r="2.5"/><circle cx="262" cy="392" r="2.5"/>
        <circle cx="165" cy="405" r="2.5"/><circle cx="178" cy="415" r="2.5"/><circle cx="192" cy="410" r="2.5"/><circle cx="206" cy="420" r="2.5"/><circle cx="220" cy="408" r="2.5"/><circle cx="234" cy="424" r="2.5"/><circle cx="248" cy="414" r="2.5"/><circle cx="262" cy="430" r="2.5"/><circle cx="278" cy="418" r="2.5"/><circle cx="294" cy="436" r="2.5"/><circle cx="310" cy="412" r="2.5"/><circle cx="326" cy="428" r="2.5"/><circle cx="350" cy="420" r="2.5"/><circle cx="368" cy="440" r="2.5"/><circle cx="382" cy="412" r="2.5"/><circle cx="428" cy="442" r="2.5"/><circle cx="172" cy="440" r="2.5"/><circle cx="186" cy="448" r="2.5"/><circle cx="200" cy="438" r="2.5"/><circle cx="214" cy="452" r="2.5"/><circle cx="228" cy="444" r="2.5"/><circle cx="244" cy="458" r="2.5"/><circle cx="260" cy="448" r="2.5"/><circle cx="276" cy="460" r="2.5"/><circle cx="300" cy="452" r="2.5"/><circle cx="344" cy="455" r="2.5"/>
        <circle cx="164" cy="476" r="2.5"/><circle cx="176" cy="486" r="2.5"/><circle cx="190" cy="478" r="2.5"/><circle cx="204" cy="492" r="2.5"/><circle cx="218" cy="482" r="2.5"/><circle cx="232" cy="498" r="2.5"/><circle cx="246" cy="486" r="2.5"/><circle cx="262" cy="500" r="2.5"/><circle cx="276" cy="488" r="2.5"/><circle cx="168" cy="506" r="2.5"/><circle cx="182" cy="514" r="2.5"/><circle cx="196" cy="508" r="2.5"/><circle cx="210" cy="518" r="2.5"/><circle cx="226" cy="510" r="2.5"/><circle cx="166" cy="520" r="2.5"/><circle cx="288" cy="516" r="2.5"/><circle cx="320" cy="480" r="2.5"/><circle cx="402" cy="486" r="2.5"/><circle cx="446" cy="516" r="2.5"/><circle cx="240" cy="520" r="2.5"/>
      </g>
      <line class="trend" x1="155" y1="457" x2="600" y2="315" stroke="var(--navy)" stroke-width="3.5"/>
      <g class="band-labels sans" font-size="19" font-weight="700" fill="var(--navy)">
        <text x="478" y="306">POOR</text><text x="478" y="377">FAIR</text><text x="478" y="430">GOOD</text><text x="478" y="490">EXCELLENT</text>
      </g>
      <g class="y-ticks serif" font-size="19" fill="#333" text-anchor="end">
        <text x="144" y="238">2,500</text><text x="144" y="284">2,000</text><text x="144" y="344">1,500</text><text x="144" y="403">1,000</text><text x="144" y="464">500</text>
      </g>
      <text transform="translate(62 420) rotate(-90)" class="sans" font-size="15" fill="var(--ink-soft)" letter-spacing="1">VEX-QT SCORE</text>
      <g class="x-ticks serif" font-size="19" fill="#333" text-anchor="middle">
        <text x="212" y="566">5</text><text x="279" y="566">10</text><text x="342" y="566">15</text><text x="406" y="566">20</text><text x="468" y="566">25</text><text x="532" y="566">30</text><text x="594" y="566">35</text>
      </g>
      <text x="362" y="597" class="sans" font-size="18" fill="var(--ink-soft)" text-anchor="middle">Years Since Diagnosis</text>
      <g class="legend sans">
        <rect x="620" y="222" width="21" height="20" fill="var(--red)"/>
        <text x="653" y="239" font-size="20" font-weight="600" fill="var(--red)">HIGHER VEX-QT</text>
        <g font-size="12.5" fill="#555" letter-spacing="1.3">
          <circle cx="662" cy="267" r="2.5" fill="var(--red)"/><text x="681" y="272">DAIRY</text>
          <circle cx="662" cy="292" r="2.5" fill="var(--red)"/><text x="681" y="297">BEEF</text>
          <circle cx="662" cy="317" r="2.5" fill="var(--red)"/><text x="681" y="322">CANNED FRUITS &amp; VEGGIES</text>
          <circle cx="662" cy="342" r="2.5" fill="var(--red)"/><text x="681" y="347">FRIED FOODS</text>
          <circle cx="662" cy="370" r="2.5" fill="var(--red)"/><text x="681" y="375">SODA</text>
        </g>
        <rect x="620" y="396" width="21" height="20" fill="var(--green)"/>
        <text x="653" y="413" font-size="20" font-weight="600" fill="var(--green)">LOWER VEX-QT</text>
        <g font-size="12.5" fill="#555" letter-spacing="1.3">
          <circle cx="662" cy="439" r="2.5" fill="var(--green)"/><text x="681" y="444">FRESH FRUITS</text><text x="681" y="460">&amp; VEGGIES</text>
          <circle cx="662" cy="483" r="2.5" fill="var(--green)"/><text x="681" y="488">NUTS &amp; SEEDS</text>
          <circle cx="662" cy="508" r="2.5" fill="var(--green)"/><text x="681" y="513">OLIVE &amp; COCONUT OIL</text>
          <circle cx="662" cy="536" r="2.5" fill="var(--green)"/><text x="681" y="541">FRESH HERB &amp; SPICES</text>
          <circle cx="662" cy="562" r="2.5" fill="var(--green)"/><text x="681" y="567">NON-FRIED FISH</text>
          <circle cx="662" cy="592" r="2.5" fill="var(--green)"/><text x="681" y="597">WINE</text>
        </g>
      </g>
    </svg>
  </section>

  <!-- Dietary behaviours panel -->
  <section class="panel panel-behaviors">
    <svg width="624" height="338" viewBox="20 623 780 422">
      <path d="M20 623 H770 a30 30 0 0 1 30 30 V671 H20 Z" fill="var(--band-head)"/>
      <text x="89" y="657" class="serif" font-size="27" fill="#fff" letter-spacing="1">Impact of dietary behaviors on PD progression</text>
      <g stroke="#e2e1dc" stroke-width="1.5">
        <line x1="556" y1="678" x2="556" y2="1015"/><line x1="678" y1="678" x2="678" y2="1015"/><line x1="740" y1="678" x2="740" y2="1015"/>
      </g>
      <g class="tracks" fill="var(--track)">
        <rect x="500" y="689" width="118" height="12"/><rect x="500" y="717" width="118" height="12"/><rect x="500" y="745" width="118" height="12"/><rect x="500" y="773" width="118" height="12"/><rect x="500" y="801" width="118" height="12"/><rect x="500" y="829" width="118" height="12"/><rect x="500" y="857" width="118" height="12"/><rect x="500" y="885" width="118" height="12"/><rect x="500" y="913" width="118" height="12"/><rect x="500" y="942" width="118" height="12"/>
        <rect x="618" y="971" width="120" height="12"/><rect x="618" y="999" width="120" height="12"/>
      </g>
      <g class="bars-good" fill="var(--green-bright)">
        <rect x="576" y="689" width="42" height="12" rx="6"/><rect x="579" y="717" width="39" height="12" rx="6"/><rect x="585" y="745" width="33" height="12" rx="6"/><rect x="586" y="773" width="32" height="12" rx="6"/><rect x="587" y="801" width="31" height="12" rx="6"/><rect x="590" y="829" width="28" height="12" rx="6"/><rect x="592" y="857" width="26" height="12" rx="6"/><rect x="596" y="885" width="22" height="12" rx="6"/><rect x="597" y="913" width="21" height="12" rx="6"/><rect x="600" y="942" width="18" height="12" rx="6"/>
      </g>
      <g class="bars-bad" fill="var(--red)">
        <rect x="618" y="971" width="108" height="12" rx="6"/><rect x="618" y="999" width="114" height="12" rx="6"/>
      </g>
      <g class="sans" font-size="14.5" fill="#444" text-anchor="end">
        <text x="416" y="694">I cook most of my meals</text><text x="416" y="720">I avoid artificial sweetners</text><text x="416" y="747">I avoid soda</text><text x="416" y="776">I avoid artificial colors, flavors</text><text x="416" y="806">I routinely prepare meals for others</text><text x="416" y="834">I avoid dairy</text><text x="416" y="862">I try to eat organically grown foods when possible</text><text x="416" y="890">I avoid pork</text><text x="416" y="918">I buy from local farmers</text><text x="416" y="947">I avoid beef</text><text x="416" y="975">I find it difficult to afford healthy food</text><text x="416" y="1002">It is difficult to afford groceries</text>
      </g>
      <g class="serif" font-size="20" fill="var(--green-bright)">
        <text x="441" y="696">-146</text><text x="441" y="723">-121</text><text x="441" y="748">-108</text><text x="441" y="778">-106</text><text x="441" y="809">-105</text><text x="441" y="837">-92</text><text x="441" y="864">-86</text><text x="441" y="892">-75</text><text x="441" y="920">-71</text><text x="441" y="949">-63</text>
        <text x="441" y="977" fill="var(--red)">366</text><text x="441" y="1004" fill="var(--red)">389</text>
      </g>
      <g class="sans" font-size="12" fill="#444" text-anchor="middle">
        <text x="498" y="1034">-400</text><text x="556" y="1034">-200</text><text x="618" y="1034">0</text><text x="678" y="1034">200</text><text x="740" y="1034">400</text>
      </g>
    </svg>
  </section>

  <!-- Servings panel -->
  <section class="panel panel-servings">
    <svg width="476" height="688" viewBox="885 150 595 860">
      <g class="axis-top serif" font-size="16" text-anchor="middle">
        <text x="1138" y="177" fill="var(--green)">-300</text><text x="1205" y="177" fill="var(--green)">-150</text><text x="1267" y="177" fill="#666">0</text><text x="1333" y="177" fill="var(--red)">150</text><text x="1400" y="177" fill="var(--red)">300</text>
      </g>
      <g stroke="#ececec" stroke-width="1.5">
        <line x1="1140" y1="185" x2="1140" y2="935"/><line x1="1400" y1="185" x2="1400" y2="935"/>
        <line x1="1005" y1="215" x2="1400" y2="215"/><line x1="1005" y1="248" x2="1400" y2="248"/><line x1="1005" y1="280" x2="1400" y2="280"/><line x1="1005" y1="313" x2="1400" y2="313"/><line x1="1005" y1="345" x2="1400" y2="345"/><line x1="1005" y1="378" x2="1400" y2="378"/><line x1="1005" y1="410" x2="1400" y2="410"/><line x1="1005" y1="443" x2="1400" y2="443"/><line x1="1005" y1="475" x2="1400" y2="475"/><line x1="1005" y1="508" x2="1400" y2="508"/><line x1="1005" y1="540" x2="1400" y2="540"/><line x1="1005" y1="573" x2="1400" y2="573"/><line x1="1005" y1="605" x2="1400" y2="605"/><line x1="1005" y1="638" x2="1400" y2="638"/><line x1="1005" y1="670" x2="1400" y2="670"/><line x1="1005" y1="703" x2="1400" y2="703"/><line x1="1005" y1="735" x2="1400" y2="735"/><line x1="1005" y1="768" x2="1400" y2="768"/><line x1="1005" y1="800" x2="1400" y2="800"/><line x1="1005" y1="833" x2="1400" y2="833"/><line x1="1005" y1="865" x2="1400" y2="865"/><line x1="1005" y1="898" x2="1400" y2="898"/>
      </g>
      <g class="tracks" fill="#e6e6e6">
        <rect x="1140" y="202" width="128" height="14"/><rect x="1140" y="235" width="128" height="14"/><rect x="1140" y="267" width="128" height="14"/><rect x="1140" y="300" width="128" height="14"/><rect x="1140" y="332" width="128" height="14"/><rect x="1140" y="365" width="128" height="14"/><rect x="1140" y="397" width="128" height="14"/><rect x="1140" y="430" width="128" height="14"/>
        <rect x="1268" y="462" width="132" height="14"/><rect x="1268" y="495" width="132" height="14"/><rect x="1268" y="527" width="132" height="14"/><rect x="1268" y="560" width="132" height="14"/><rect x="1268" y="592" width="132" height="14"/><rect x="1268" y="625" width="132" height="14"/><rect x="1268" y="657" width="132" height="14"/><rect x="1268" y="690" width="132" height="14"/><rect x="1268" y="722" width="132" height="14"/><rect x="1268" y="755" width="132" height="14"/><rect x="1268" y="787" width="132" height="14"/><rect x="1268" y="820" width="132" height="14"/><rect x="1268" y="852" width="132" height="14"/><rect x="1268" y="885" width="132" height="14"/><rect x="1268" y="917" width="132" height="14"/>
      </g>
      <g class="bars-good" fill="var(--green)">
        <rect x="1171" y="201" width="99" height="15" rx="7"/><rect x="1185" y="234" width="85" height="15" rx="7"/><rect x="1197" y="266" width="73" height="15" rx="7"/><rect x="1205" y="299" width="65" height="15" rx="7"/><rect x="1216" y="331" width="54" height="15" rx="7"/><rect x="1217" y="364" width="53" height="15" rx="7"/><rect x="1233" y="396" width="37" height="15" rx="7"/><rect x="1241" y="429" width="29" height="15" rx="7"/>
      </g>
      <g class="bars-bad" fill="var(--red)">
        <rect x="1266" y="461" width="23" height="15" rx="7"/><rect x="1266" y="494" width="27" height="15" rx="7"/><rect x="1266" y="526" width="29" height="15" rx="7"/><rect x="1266" y="559" width="32" height="15" rx="7"/><rect x="1266" y="591" width="34" height="15" rx="7"/><rect x="1266" y="624" width="34" height="15" rx="7"/><rect x="1266" y="656" width="35" height="15" rx="7"/><rect x="1266" y="689" width="41" height="15" rx="7"/><rect x="1266" y="721" width="42" height="15" rx="7"/><rect x="1266" y="754" width="51" height="15" rx="7"/><rect x="1266" y="786" width="53" height="15" rx="7"/><rect x="1266" y="819" width="58" height="15" rx="7"/><rect x="1266" y="851" width="64" height="15" rx="7"/><rect x="1266" y="884" width="66" height="15" rx="7"/><rect x="1266" y="916" width="87" height="15" rx="7"/>
      </g>
      <g class="sans" font-size="18.5" text-anchor="end" letter-spacing="0.8">
        <g fill="var(--green)">
          <text x="1120" y="205">FRESH VEGETABLES</text><text x="1120" y="238">FRESH FRUITS</text><text x="1120" y="270">NUTS/SEEDS</text><text x="1120" y="303">FISH</text><text x="1120" y="335">WINE</text><text x="1120" y="368">OLIVE OIL</text><text x="1120" y="400">COCONUT OIL</text><text x="1120" y="433">FRESH HERBS</text>
        </g>
        <g fill="var(--red)">
          <text x="1120" y="465">MILK</text><text x="1120" y="498">CHEESE</text><text x="1120" y="530">YOGURT</text><text x="1120" y="563">FROZEN VEGETABLES</text><text x="1120" y="595">PORK</text><text x="1120" y="628">CHICKEN</text><text x="1120" y="660">PLASTIC-BOTTLED DRINKS</text><text x="1120" y="693">SODA</text><text x="1120" y="725">PASTA</text><text x="1120" y="758">BEEF</text><text x="1120" y="790">CANNED VEG</text><text x="1120" y="823">ICE CREAM</text><text x="1120" y="855">FRIED FOODS</text><text x="1120" y="888">DIET SODA</text><text x="1120" y="920">CANNED FRUIT</text>
        </g>
      </g>
      <g class="serif" font-size="21">
        <g fill="var(--green)">
          <text x="1279" y="206">-225</text><text x="1279" y="238">-188</text><text x="1279" y="271">-161</text><text x="1279" y="304">-144</text><text x="1279" y="336">-115</text><text x="1279" y="369">-114</text><text x="1279" y="401">-79</text><text x="1279" y="433">-58</text>
        </g>
        <g fill="#666" text-anchor="end">
          <text x="1244" y="464">42</text><text x="1240" y="497">51</text><text x="1244" y="529">56</text><text x="1244" y="562">63</text><text x="1244" y="595">67</text><text x="1244" y="627">68</text><text x="1244" y="660">69</text><text x="1244" y="692">84</text><text x="1244" y="724">86</text><text x="1252" y="757">106</text><text x="1252" y="789">110</text><text x="1252" y="822">120</text><text x="1252" y="855">144</text><text x="1252" y="887">146</text><text x="1249" y="920">191</text>
        </g>
      </g>
      <g class="axis-bottom serif" font-size="16" text-anchor="middle">
        <text x="1138" y="963" fill="var(--green)">-300</text><text x="1205" y="963" fill="var(--green)">-150</text><text x="1267" y="963" fill="#666">0</text><text x="1333" y="963" fill="var(--red)">150</text><text x="1400" y="963" fill="var(--red)">300</text>
      </g>
      <g class="sans" font-size="12" fill="var(--sky)" text-anchor="middle">
        <text x="1268" y="980">Never</text><text x="1268" y="995">Consume</text>
      </g>
    </svg>
  </section>

  <div class="footer-tab">www.wellfedwithqt.org</div>
</div>
</body>
</html>
```